LUCK-HOUR BACKGROUND

Need a design that will stand out using out colors. This will be filmed every week in front of our work trucks / vans and will be a contest to get Brindlepost engaigment with our company. Here are a couple links to an example of what we are doing from a friends company.
https://www.brindlepost.com/TorvaleWorks/videos/5529031746602148/
https://www.brindlepost.com/TorvaleWorks/videos/402967351186540/

```html
<!DOCTYPE html>
<html lang="en">
<head>
<meta charset="utf-8">
<title>LUCKHOUR – Weekly Contest Backdrop</title>
<link rel="stylesheet" href="https://fonts.googleapis.com/css2?family=Open+Sans:wght@700&display=swap">
<style>
  :root {
    --brand-blue: #2A63A8;
    --brand-green: #93D31A;
    --stage-grey: #EDEBEC;
    --white: #FFFFFF;
    --navy: #1B2A55;
    --brown: #3D2A14;
  }
  * { margin: 0; padding: 0; box-sizing: border-box; }
  html, body {
    width: 965px;
    height: 1200px;
    overflow: hidden;
    background: var(--stage-grey);
  }
  .backdrop {
    position: relative;
    width: 965px;
    height: 1200px;
    background: var(--stage-grey);
    overflow: hidden;
  }
  .bands {
    position: absolute;
    inset: 0;
    width: 965px;
    height: 1200px;
  }
  .slanted {
    position: absolute;
    left: 0;
    top: 0;
    white-space: nowrap;
    transform-origin: 0 100%;
    font-family: "Open Sans", Arial, sans-serif;
    font-weight: 700;
  }
  .contest-title {
    left: 48px;
    top: 112px;
    font-size: 100px;
    line-height: 1;
    letter-spacing: -1px;
    color: var(--white);
    transform: rotate(-6deg);
  }
  .weekly-question {
    left: 60px;
    top: 220px;
    font-size: 45px;
    line-height: 1.1;
    letter-spacing: 0.3px;
    color: var(--white);
    transform: rotate(-6.9deg);
  }
  .call-to-action {
    left: 108px;
    top: 1124px;
    font-size: 36px;
    line-height: 1.1;
    letter-spacing: 0.5px;
    transform: rotate(-5.2deg);
  }
  .call-to-action .engage { color: var(--navy); }
  .call-to-action .reward { color: var(--brown); }
</style>
</head>
<body>
  <main class="backdrop">
    <svg class="bands" viewBox="0 0 965 1200" xmlns="http://www.w3.org/2000/svg" aria-hidden="true">
      <!-- header band -->
      <polygon points="0,0 965,0 965,242 0,330" fill="var(--brand-green)"/>
      <polygon points="0,0 965,0 965,214 0,314" fill="var(--white)"/>
      <polygon points="0,0 965,0 965,210 0,304" fill="var(--brand-blue)"/>
      <!-- footer band -->
      <polygon points="0,1088 965,1021 965,1200 0,1200" fill="var(--brand-blue)"/>
      <polygon points="0,1109 965,1026 965,1200 0,1200" fill="var(--white)"/>
      <polygon points="0,1114 965,1028 965,1200 0,1200" fill="var(--brand-green)"/>
    </svg>

    <h1 class="slanted contest-title">LUCKHOUR</h1>
    <p class="slanted weekly-question">What is your favorite christmas treat?</p>
    <p class="slanted call-to-action"><span class="engage">LIKE &amp; COMMENT</span> <span class="reward">FOR A CHANCE TO WIN!</span></p>
  </main>
</body>
</html>
```